New local Orchid nursery branding

We need a business card designed for our small local company in Darwin, Australia that grows orchids, called Blooms at Carrow.
We will be running private sales from our property, and handing these out at local events for perspective customers.

We would like to see designs that are simple, and able to be used with minimal colours and containing an orchid, preferably a stylised representation instead of a photo.
The eventual hope is to take this into larger formats to create our company logo/branding etc, but for now we just need business cards.

Target Market(s)

Local Orchid

Industry/Entity Type

Business

Contact Information for Business Card

Company Name
Logo
Name
Phone Number
Street Address
Email Address (less prominent than rest of the text)

Font styles to use
Sans Serif

Requirements
Must have
• Name of the company, which is Blooms at Carrow
Nice to have
• stylised orchid logo
Should not have
• too many colours

```html
<!DOCTYPE html>
<html lang="en">
<head>
<meta charset="utf-8">
<title>Blooms at Carrow — Business Card</title>
<link rel="stylesheet" href="https://fonts.googleapis.com/css2?family=Pinyon+Script&family=EB+Garamond:wght@400;500;600&display=swap">
<style>
  :root {
    --backdrop: #bbbcbe;
    --card: #ffffff;
    --magenta: #e0197a;
    --ink: #4a4a4a;
    --petal-light: #f9c3dc;
    --petal-mid: #ef7fb3;
    --petal-deep: #d9338a;
  }
  html, body {
    margin: 0;
    width: 1200px;
    height: 1200px;
    overflow: hidden;
    background: var(--backdrop);
  }
  .card {
    position: absolute;
    left: 100px;
    top: 315px;
    width: 1000px;
    height: 571px;
    background: var(--card);
    box-shadow: 0 18px 40px rgba(0,0,0,0.18);
    overflow: hidden;
  }
  .floral {
    position: absolute;
    inset: 0;
    width: 100%;
    height: 100%;
  }
  .brand {
    position: absolute;
    left: 0;
    right: 0;
    top: 72px;
    margin: 0;
    padding-left: 60px;
    text-align: center;
    font-family: "Pinyon Script", cursive;
    font-weight: 400;
    font-size: 66px;
    color: var(--magenta);
    line-height: 1;
  }
  .brand-rule {
    position: absolute;
    left: 300px;
    width: 490px;
    top: 152px;
    height: 1.5px;
    background: var(--magenta);
  }
  .details {
    position: absolute;
    left: 0;
    right: 0;
    top: 168px;
    padding-left: 60px;
    text-align: center;
    font-family: "EB Garamond", serif;
    color: var(--ink);
  }
  .person {
    margin: 0 0 12px;
    font-size: 46px;
    font-weight: 600;
    letter-spacing: -0.5px;
    line-height: 1.2;
  }
  .person .divider {
    display: inline-block;
    width: 1.5px;
    height: 38px;
    background: var(--ink);
    margin: 0 12px 0 16px;
    vertical-align: -3px;
  }
  .person .role {
    font-size: 22px;
    font-weight: 400;
    vertical-align: 14px;
  }
  .address {
    margin: 0;
    font-size: 23px;
    line-height: 1.4;
    font-style: normal;
  }
  .contact {
    margin: 12px 0 0;
    font-size: 23px;
  }
  .contact .sep { margin: 0 8px; }
</style>
</head>
<body>
  <section class="card">
    <svg class="floral" viewBox="0 0 1000 571" xmlns="http://www.w3.org/2000/svg">
      <defs>
        <radialGradient id="bloom" cx="55%" cy="45%" r="65%">
          <stop offset="0%" stop-color="var(--petal-deep)"/>
          <stop offset="50%" stop-color="var(--petal-mid)"/>
          <stop offset="100%" stop-color="var(--petal-light)"/>
        </radialGradient>
      </defs>
      <path role="img" aria-label="Stylised pink orchid blooms with green leaves in the top right corner"
            fill="url(#bloom)" opacity="0.9"
            d="M580 0 L1000 0 L1000 190 Q965 185 945 165 Q900 120 850 95 Q800 70 760 50 Q700 40 650 35 Q600 30 580 0 Z"/>
      <path role="img" aria-label="Stylised pink orchid at the right edge"
            fill="url(#bloom)" opacity="0.9"
            d="M1000 215 Q965 225 950 260 Q940 300 975 330 L1000 340 Z"/>
      <path role="img" aria-label="Stylised pink orchid at the left edge"
            fill="url(#bloom)" opacity="0.9"
            d="M0 85 Q50 80 90 110 Q120 150 95 200 Q70 240 25 245 L0 240 Z"/>
      <path role="img" aria-label="Stylised cluster of pink orchids with green leaves along the bottom left"
            fill="url(#bloom)" opacity="0.9"
            d="M0 290 Q50 280 95 305 Q150 340 200 385 Q250 410 320 420 Q380 425 430 440 Q470 460 480 500 Q470 540 440 571 L0 571 Z"/>
    </svg>

    <h1 class="brand">Blooms at Carrow</h1>
    <div class="brand-rule"></div>

    <div class="details">
      <p class="person">John Doe<span class="divider"></span><span class="role">Director</span></p>
      <address class="address">Dummy City<br>Dummy Country Dummy Land</address>
      <p class="contact">+63 900 555 0142<span class="sep">|</span>john@bloomsatcarrow.com</p>
    </div>
  </section>
</body>
</html>
```